Indie musician needs album cover art

I am an independant musician releasing my second album via digital sources. I plan to make it available on Songvault and other digital stores but primarily distribute it free through Tunebarn.

The album's music style is a blend of singer-songwriter folk, punk, alt country, electronic rock and spoken word. The lyrical content is a dark journey through travel in foreign countries, relationships, airports and theatres, formed during my own journey as an audio engineer for a travelling theatre show.

The album is called "Lo Find Quiet" - at times both a plea and a directive. I would like the album cover to reflect a sense of longing, restlessness, unease and movement. A subversive tone is also possible.

I have had a go at designing a couple of ideas myself, using my own photos. I like the ideas but I am not skilled in graphic design and am unable to take them further to get the right feel and look. I will post these as examples of tone. The finished work does not need to copy either of these.

A .zip of the album can be downloaded here (low fi mp3):

http://qlnk.example/Xr7tP4

Target Market(s)

People who enjoy thoughtful, honest, homemade music. Definitely not a teeny pop audience. Adult, subversive, educated, emotional...

Industry/Entity Type

Graphic Design

Requirements
Must have
• Artist name (no caps): kestrin
Album name (prefer no caps): lo find quiet

```html
<!DOCTYPE html>
<html lang="en">
<head>
<meta charset="utf-8">
<title>kestrin — lo find quiet</title>
<link rel="stylesheet" href="https://fonts.googleapis.com/css2?family=Open+Sans:wght@400&family=Share+Tech+Mono&display=swap">
<style>
  :root {
    --ink: #000000;
    --yellow: #d8c531;
    --amber: #e0a22a;
    --orange: #d9661c;
    --artist: #f27a3a;
  }
  * { margin: 0; padding: 0; box-sizing: border-box; }
  html, body { width: 1200px; height: 847px; overflow: hidden; background: var(--ink); }
  .cover {
    position: relative;
    width: 1200px;
    height: 847px;
    background: var(--ink);
    overflow: hidden;
  }
  .water-photo {
    position: absolute;
    left: 110px;
    top: 70px;
    width: 1020px;
    height: 760px;
    border-radius: 50%;
    background:
      radial-gradient(ellipse at 50% 45%, rgba(0,0,0,0) 0%, rgba(0,0,0,0) 45%, rgba(0,0,0,0.55) 68%, rgba(0,0,0,1) 72%),
      linear-gradient(90deg, var(--yellow) 0%, #c9b62c 25%, var(--amber) 55%, var(--orange) 80%, #a8400f 100%);
    opacity: 0.85;
  }
  .title-band {
    position: absolute;
    left: 0;
    top: 494px;
    width: 1200px;
    height: 110px;
  }
  .album-title {
    position: absolute;
    left: 0;
    width: 1200px;
    top: 488px;
    text-align: center;
    padding-left: 0;
    font-family: "Open Sans", "Myriad Pro", sans-serif;
    font-weight: 400;
    font-size: 112px;
    line-height: 120px;
    letter-spacing: -1px;
    color: var(--ink);
  }
  .artist-name {
    position: absolute;
    right: 16px;
    top: 18px;
    font-family: "Share Tech Mono", monospace;
    font-size: 62px;
    line-height: 72px;
    letter-spacing: 5px;
    color: var(--artist);
  }
</style>
</head>
<body>
  <main class="cover">
    <div class="water-photo" role="img" aria-label="Photograph from above of two swimmers floating with arms outstretched in rippling water, toned yellow to orange"></div>

    <svg class="title-band" viewBox="0 0 1200 110" aria-hidden="true">
      <defs>
        <linearGradient id="bandTone" x1="0" x2="1" y1="0" y2="0">
          <stop offset="0" stop-color="#d8c531" stop-opacity="0"/>
          <stop offset="0.16" stop-color="#e0d03a" stop-opacity="0.9"/>
          <stop offset="0.5" stop-color="#eca92c"/>
          <stop offset="0.84" stop-color="#e06a1e" stop-opacity="0.9"/>
          <stop offset="1" stop-color="#d9661c" stop-opacity="0"/>
        </linearGradient>
        <linearGradient id="streakTone" x1="0" x2="1" y1="0" y2="0">
          <stop offset="0" stop-color="#d8c531" stop-opacity="0"/>
          <stop offset="0.2" stop-color="#d8c531" stop-opacity="0.7"/>
          <stop offset="0.8" stop-color="#e06a1e" stop-opacity="0.7"/>
          <stop offset="1" stop-color="#d9661c" stop-opacity="0"/>
        </linearGradient>
      </defs>
      <rect class="band-core" x="210" y="6" width="780" height="98" fill="url(#bandTone)"/>
      <g class="band-streaks" fill="url(#streakTone)">
        <rect x="20" y="14" width="1160" height="2"/>
        <rect x="60" y="24" width="1100" height="3"/>
        <rect x="10" y="36" width="1180" height="2"/>
        <rect x="90" y="46" width="1040" height="4"/>
        <rect x="30" y="58" width="1150" height="2"/>
        <rect x="70" y="68" width="1080" height="3"/>
        <rect x="15" y="80" width="1170" height="2"/>
        <rect x="110" y="92" width="1000" height="3"/>
      </g>
    </svg>

    <h1 class="album-title">lo find quiet</h1>
    <p class="artist-name">kestrin</p>
  </main>
</body>
</html>
```